Wes Hadley Golf Teaching Rack Card

The flyer will be a rack card. Front side only. Nothing on back. 3.75 inches by 8.5 inches. Or close to that. I’d like it to be as colorful as possible and to include several logos in different places.
The brochure is to attract golfers attention and still look traditional and classy not crazy or to artsy. Golf is a very traditional sport and would just like it to look professional and welcoming so golfers no I’m credible in my teaching and they will learn something. I will send a rough idea and a sample of one I had before but use your creative skills and ingenuity to design it. You will have to put my name: Wes Hadley under the NLT logo. It is a requirement by the NLT. Also the logo size must me .0875 inches high. If possible use a gotham or Hoefler text type or something businesslike or similar for my name. Also I am sorry for the different logos available on this file because I am not tech savvy so you will have to choose the best logo and cut it out of the grouping to match what you want to do. I am sorry for all the details. I will be available all weekend if you need more info. or help. I am sure you are very skilled and can tell I am not. Sorry. I laid out a sketch for you so you know what info. verbiage is important. and where to somewhat place the logos. Up to your skill for most of it. Your design! Go for it.!

Target Market(s)

Golfers of all ages from 18-70. Men and Women.

Industry/Entity Type

Golf Industry. Teaching and learning game if golf

Font styles to use
Sans Serif
Other font styles liked:
• Mixture maybe traditional type. Easy to read.

Colors

Designer to choose only greyscale colors for use in the design.

Requirements
Must have
• My JPG golf logo and the NLT official logo. Also will send several other logos to put in. I will tell you where they should go on the rack card.
Nice to have
• Maybe a golf picture from a course with a green and flag as the one on my old brochure I’m sending or similar. It just adds color and eye catching
Should not have
• Nothing hard to read or difficult to comprehend. Pretty straight forward and quality and style in a traditional sense,

```html
<!DOCTYPE html>
<html lang="en">
<head>
<meta charset="utf-8">
<title>Wes Hadley Golf Rack Card</title>
<link rel="stylesheet" href="https://fonts.googleapis.com/css2?family=Poppins:wght@400;500;600;700;800;900&family=Oswald:wght@500;600&family=Montserrat:wght@500;600;700&display=swap">
<style>
:root{
  --light:#8f8f8f;
  --dark:#2e2e2e;
  --deep:#1e1e1e;
  --mid:#6f6f6f;
  --accent:#4a4a4a;
  --ink:#111111;
  --band:#ececec;
  --page:#eeeeee;
  --white:#ffffff;
}
*{box-sizing:border-box;margin:0;padding:0}
html,body{width:1200px;height:2400px;overflow:hidden;background:var(--page)}
body{font-family:"Poppins",sans-serif;color:var(--ink)}
.card{position:absolute;left:70px;top:0;width:1060px;height:2400px;background:var(--white);overflow:hidden}
.abs{position:absolute}

.brand{left:0;width:100%;top:110px;text-align:center;color:var(--dark);font-weight:700}
.brand-mark{display:inline-block;width:110px;height:110px;border-radius:50%;background:var(--dark);vertical-align:middle;margin-right:22px}
.brand-name{display:inline-block;vertical-align:middle;font-size:54px;line-height:1.05;text-align:left}

.frame{left:48px;top:438px;width:971px;height:485px;border:2px solid var(--dark);border-bottom:none;border-radius:14px 14px 0 0}
.frame-gap{left:270px;top:430px;width:520px;height:20px;background:var(--white)}
.headline{left:0;width:100%;top:330px;text-align:center;font-weight:900;color:var(--light);font-size:245px;line-height:1;letter-spacing:-4px}
.subhead{left:0;width:100%;top:545px;text-align:center;font-weight:800;font-size:84px;line-height:1;letter-spacing:1px}

.price{left:117px;top:655px;width:427px;height:155px;background:var(--mid);border-radius:14px;color:var(--white);font-family:"Oswald",sans-serif;font-weight:600;font-size:138px;line-height:155px;text-align:center}
.duration{left:580px;top:655px;font-weight:800;font-size:30px;line-height:36px;letter-spacing:1px}
.offer{left:580px;top:713px;width:320px;height:97px;background:var(--mid);border-radius:12px;color:var(--white);font-weight:700;font-size:26px;line-height:32px;padding:18px 0 0 22px}
.reg-badge{left:826px;top:702px;width:126px;height:126px}
.reg-badge polygon{fill:var(--dark)}
.reg-text{left:826px;top:735px;width:126px;text-align:center;color:var(--white);font-family:"Oswald",sans-serif;font-weight:500;font-size:23px;line-height:29px}

.includes-band{left:0;top:837px;width:100%;height:165px;background:var(--band)}
.includes-label{font-weight:700;color:var(--dark);font-size:26px;transform:rotate(-90deg);transform-origin:left top;white-space:nowrap}
.feature{font-weight:500;font-size:25px;line-height:28px;white-space:nowrap}
.tick{display:inline-block;width:14px;height:14px;border-radius:50%;background:var(--dark);margin-right:10px;vertical-align:2px}
.feature .text{display:inline-block;vertical-align:top}
.level{left:753px;top:837px;width:216px;height:165px;background:var(--dark);border-radius:16px;color:var(--white);text-align:center}
.level-title{font-weight:700;font-size:26px;line-height:30px;padding-top:18px}
.level-info{border-top:2px solid var(--white);margin-top:16px;padding-top:14px;font-size:19px;line-height:22px}

.course-photo{left:0;top:1002px;width:100%;height:1080px;background:
  radial-gradient(ellipse 420px 260px at 180px 110px,rgba(235,235,235,.9),rgba(235,235,235,0) 70%),
  linear-gradient(180deg,#e8e8e8 0%,#c8c8c8 10%,#8e8e8e 30%,#707070 50%,#5e5e5e 70%,#4c4c4c 100%)}
.partners{left:0;width:100%;top:1080px;text-align:center;font-weight:800;font-size:62px;color:var(--white)}
.partners span{margin:0 34px}

.package{left:73px;top:1527px;width:923px;height:430px;background:rgba(30,30,30,.82);border-radius:22px}
.ribbon{left:122px;top:1513px;width:811px;height:72px;background:var(--accent);clip-path:polygon(0 0,100% 0,96% 100%,4% 100%);color:var(--white);font-weight:800;font-size:41px;line-height:72px;text-align:center;letter-spacing:1px}
.lesson-box{left:198px;top:1613px;width:348px;height:145px;background:var(--mid);border-radius:12px;overflow:hidden;text-align:center}
.lesson-head{background:var(--light);color:var(--white);font-weight:500;font-size:27px;height:56px;line-height:56px;margin:0 6px;border-radius:0 0 8px 8px}
.lesson-reg{color:var(--white);font-family:"Oswald",sans-serif;font-weight:500;font-size:52px;line-height:86px}
.deal-box{left:572px;top:1613px;width:278px;height:145px;background:var(--mid);border-radius:12px;overflow:hidden;text-align:center;color:var(--white)}
.deal-price{background:var(--light);margin:0 6px;border-radius:0 0 8px 8px;font-family:"Oswald",sans-serif;font-weight:600;font-size:72px;line-height:92px}
.deal-note{font-size:30px;line-height:52px}
.package-label{color:var(--light)}
.package-list .feature{color:var(--white);font-size:25px}
.package-list .tick{background:var(--light)}

.wave-white{fill:var(--white)}
.wave-dark{fill:var(--dark)}
.wave-light{fill:var(--light)}

.contact{left:106px;top:2158px;font-family:"Montserrat",sans-serif;font-weight:600;font-size:29px;line-height:42px}
.contact svg{width:26px;height:26px;vertical-align:-4px;margin-right:14px}
.icon-fill{fill:var(--dark)}
.icon-line{fill:none;stroke:var(--dark);stroke-width:2}
.icon-cut{fill:none;stroke:var(--white);stroke-width:2}
.seal{border-radius:50%}
.seal-guarantee{left:477px;top:2117px;width:160px;height:160px;background:var(--mid);border:8px solid var(--ink)}
.seal-assoc{left:656px;top:2110px;width:156px;height:156px;background:var(--dark);border:8px solid var(--white);box-shadow:0 0 0 3px var(--dark)}
.member-name{left:634px;top:2284px;width:200px;text-align:center;font-family:"Montserrat",sans-serif;font-weight:600;font-size:24px}
.member-note{left:850px;top:2190px;font-family:"Montserrat",sans-serif;font-weight:500;font-size:20px;line-height:24px}
</style>
</head>
<body>
<main class="card">

  <div class="abs brand"><span class="brand-mark"></span><span class="brand-name">WES HADLEY<br>GOLF</span></div>

  <div class="abs frame"></div>
  <div class="abs frame-gap"></div>
  <h1 class="abs headline">GOLF</h1>
  <h2 class="abs subhead">SWING ANALYSIS</h2>

  <div class="abs price">$59.99</div>
  <div class="abs duration">1- HOUR ANALYSIS</div>
  <div class="abs offer">*ONE TIME<br>LIMITED OFFER</div>
  <svg class="abs reg-badge" viewBox="0 0 100 100" aria-hidden="true">
    <polygon points="50,0 56,10 66,3 69,15 81,12 80,24 92,26 87,37 98,43 89,51 97,60 86,65 90,77 78,78 77,90 65,87 60,98 51,90 43,99 37,88 26,93 24,81 12,81 14,69 3,64 12,56 2,48 12,41 6,30 18,27 17,15 29,16 33,5 43,11"/>
  </svg>
  <div class="abs reg-text">REG<br>$79.00</div>

  <section class="abs includes-band"></section>
  <div class="abs includes-label" style="left:92px;top:1002px">Includes</div>
  <div class="abs feature" style="left:170px;top:852px"><span class="tick"></span><span class="text">Swing Analysis<br>w/video</span></div>
  <div class="abs feature" style="left:170px;top:923px"><span class="tick"></span><span class="text">Review of Swing<br>technique</span></div>
  <div class="abs feature" style="left:418px;top:852px"><span class="tick"></span><span class="text">Suggested Tips &amp;<br>Drills</span></div>
  <div class="abs feature" style="left:418px;top:918px"><span class="tick"></span><span class="text">Video &amp; Summary sent<br>to your Mobile Devices</span></div>
  <div class="abs level">
    <div class="level-title">Beginners to<br>Advanced</div>
    <div class="level-info">Additional INFO<br>www.WHADLEY.com</div>
  </div>

  <div class="abs course-photo" role="img" aria-label="Photo of a golf driver behind a ball on a tee on a sunlit fairway"></div>
  <div class="abs partners"><span>Swingtrack</span><span>Launchpoint</span></div>

  <section class="abs package"></section>
  <div class="abs ribbon">SPECIAL LESSON PACKAGE</div>
  <div class="abs lesson-box">
    <div class="lesson-head">3- One Hour Lessons</div>
    <div class="lesson-reg">REG: $237.00</div>
  </div>
  <div class="abs deal-box">
    <div class="deal-price">$225.00</div>
    <div class="deal-note">(Limited Deal)</div>
  </div>
  <div class="abs includes-label package-label" style="left:162px;top:1905px">Includes</div>
  <div class="package-list">
    <div class="abs feature" style="left:236px;top:1782px"><span class="tick"></span><span class="text">Video Analysis</span></div>
    <div class="abs feature" style="left:236px;top:1838px"><span class="tick"></span><span class="text">Lesson Summary<br>and Video</span></div>
    <div class="abs feature" style="left:500px;top:1782px"><span class="tick"></span><span class="text">Review sent to mobile devices</span></div>
    <div class="abs feature" style="left:500px;top:1821px"><span class="tick"></span><span class="text">Tips &amp; Drills</span></div>
    <div class="abs feature" style="left:500px;top:1860px"><span class="tick"></span><span class="text">Action Plan to Improve</span></div>
  </div>

  <svg class="abs" style="left:0;top:1880px" width="1060" height="300" viewBox="0 0 1060 300" aria-hidden="true">
    <path class="wave-white" d="M0,100 C300,10 620,30 1060,100 L1060,300 L0,300 Z"/>
    <path class="wave-dark" d="M0,125 C300,35 620,55 1060,125 L1060,300 L0,300 Z"/>
    <path class="wave-light" d="M0,235 C320,285 700,225 1060,110 L1060,300 L0,300 Z"/>
    <path class="wave-white" d="M0,265 C320,305 700,265 1060,160 L1060,300 L0,300 Z"/>
  </svg>

  <div class="abs contact">
    <div><svg viewBox="0 0 24 24"><path class="icon-fill" d="M6.6 10.8a15 15 0 0 0 6.6 6.6l2.2-2.2c.3-.3.7-.4 1-.2 1.1.4 2.3.6 3.6.6.6 0 1 .4 1 1V20c0 .6-.4 1-1 1A17 17 0 0 1 3 4c0-.6.4-1 1-1h3.5c.6 0 1 .4 1 1 0 1.3.2 2.5.6 3.6.1.3 0 .7-.2 1z"/></svg>555-014-0199</div>
    <div><svg viewBox="0 0 24 24"><rect class="icon-fill" x="2" y="5" width="20" height="14"/><path class="icon-cut" d="M2 5l10 8 10-8"/></svg>whadley@NLT.com</div>
    <div><svg viewBox="0 0 24 24"><circle class="icon-line" cx="12" cy="12" r="10"/><path class="icon-line" d="M2 12h20M12 2c3 3 3 17 0 20M12 2c-3 3-3 17 0 20"/></svg>WHADLEY.COM</div>
    <div><svg viewBox="0 0 24 24"><circle class="icon-line" cx="12" cy="12" r="10"/><path class="icon-line" d="M2 12h20M12 2c3 3 3 17 0 20M12 2c-3 3-3 17 0 20"/></svg>www.whadleyGolf.com</div>
  </div>
  <div class="abs seal seal-guarantee"></div>
  <div class="abs seal seal-assoc"></div>
  <div class="abs member-name">Wes Hadley</div>
  <div class="abs member-note">Wes Hadley<br>Class a Member<br>QTR. CENTURY<br>MEMBER NLT</div>

</main>
</body>
</html>
```